Website Design Front page Holistic Members site & Natural Therapist Directory

I need a modern, fresh unique look for a natural therapy and holistic/ Spiritual directory & educational website. It needs to be clear, colourful, inviting and suitable for both sexes - young and old. I want it look fresh and super modern.

I will require the design in .psd format and anything in the centre section including rotational image needs to be supplied in .ai so I can break down the components and colours used will also be needed for frames and banners.

Target Market(s)

all ages, male and female. It must appeal to both therapists and general public.

Requirements
Must have
• Logo obviously. Room for a video player 300 x 250. And small introduction text panel. Must follow the layout in file attached. Also a rotating image up the top, in main section (have supplied example image alter as you like - man pointing top right). Have also supplied example of text to have on it. 16 Menu bars on left frame, under home. Must have 6 prominent links to main pages of site. Have included images use if you want or else use your own. These 6 are, Find a Psychic/ Medium, Find a Natural Therapist, Find a Business/ Club/ School, Find an Event/ Workshop, Find a Product, Holistic Career Centre.I have also attached a shot of the emag, although nothing special in design, useful for complimentary colour choices but not limited to. Another link image/ banner would be Free Chat Now.Another if room and not over crowded would be compare memberships. Can use leader board and leader ad board. Also require the footer to be designed and delivered in .ai similar to craft pebble with link image to chatterly and blurbo.
Nice to have
• Compare memberships link would be great but not essential... don't want page to look too busy.
Should not have
• Must not be too busy.. think zen with a modern twist.

```html
<!DOCTYPE html>
<html lang="en">
<head>
<meta charset="utf-8">
<title>Kindred Echo – Holistic Community</title>
<link href="https://fonts.googleapis.com/css2?family=Questrial&display=swap" rel="stylesheet">
<style>
  :root{
    --page-bg-a:#f6ec9a;
    --page-bg-b:#e3cf7a;
    --column:#f5f8c8;
    --ink:#1a1a1a;
    --green-dark:#5f9a4a;
    --green-mid:#9ccb86;
    --green-light:#e9f5df;
    --sea-top:#1a7fc6;
    --sea-mid:#4aa7e0;
    --sea-low:#2a78b8;
    --pink:#e0388f;
    --orange:#f4922a;
    --lime:#8cc63f;
    --apricot:#fbb550;
    --cyan:#3fbfd1;
    --plum:#9b1f8a;
    --white:#ffffff;
  }
  *{margin:0;padding:0;box-sizing:border-box}
  html,body{width:1117px;height:1200px;overflow:hidden}
  body{
    font-family:"Questrial",sans-serif;color:var(--ink);
    background:linear-gradient(90deg,var(--page-bg-b),var(--page-bg-a) 12%,var(--page-bg-a) 88%,var(--page-bg-b));
    position:relative;
  }
  .site{position:absolute;left:110px;top:0;width:897px;height:1200px;background:var(--column);
    box-shadow:0 0 14px rgba(120,100,40,.35)}
  .utility-nav{position:absolute;right:16px;top:18px;font-size:16px;display:flex;gap:14px}
  .utility-nav span.sep{opacity:.8}
  .top-band{position:absolute;left:0;top:44px;width:897px;height:54px;
    background:linear-gradient(180deg,var(--green-dark) 0,var(--green-mid) 20%,var(--white) 55%,var(--green-mid) 85%,var(--green-dark))}
  .logo-box{position:absolute;left:37px;top:0;width:181px;height:149px;
    background:linear-gradient(135deg,#f2f7f8,#d5e2e6);display:flex;align-items:center;justify-content:center;gap:8px;z-index:3}
  .logo-dot{width:22px;height:22px;border-radius:50%;background:var(--plum)}
  .logo-name{font-size:24px;color:#2b2b2b;line-height:1}
  .hero{position:absolute;left:0;top:98px;width:897px;height:297px;overflow:hidden}
  .hero-photo{position:absolute;left:250px;top:0;width:647px;height:297px;
    background:linear-gradient(180deg,var(--sea-top) 0,var(--sea-mid) 55%,#cfe8f7 78%,var(--sea-low) 80%,#1f6aa8)}
  .hero-panel{position:absolute;left:0;top:0}
  .hero-headline{position:absolute;left:635px;top:84px;color:var(--white);font-size:33px;line-height:40px;
    text-shadow:0 1px 3px rgba(0,0,0,.25)}
  .main-nav{position:absolute;left:37px;top:164px;list-style:none;font-size:20px;line-height:33.5px;z-index:2}
  .join-btn{position:absolute;left:38px;top:341px;width:106px;height:32px;border-radius:5px;
    background:linear-gradient(180deg,#fff,#d9d9d9);box-shadow:0 1px 3px rgba(0,0,0,.4);
    display:flex;align-items:center;justify-content:center;gap:7px;font-size:16px;color:#444;z-index:2}
  .join-btn i{width:13px;height:13px;border-radius:50%;background:#555;position:relative}
  .join-btn i::after{content:"";position:absolute;left:5px;top:3.5px;border-left:5px solid #fff;border-top:3px solid transparent;border-bottom:3px solid transparent}
  .intro{position:absolute;left:37px;top:405px;width:420px}
  .intro h1{font-weight:400;font-size:30px;margin-bottom:16px;white-space:nowrap}
  .intro p{font-size:14.5px;line-height:25.6px;margin-bottom:25px}
  .video-frame{position:absolute;left:476px;top:437px;width:421px;height:276px;
    background:linear-gradient(90deg,var(--green-mid),var(--white) 50%,var(--green-mid))}
  .video-screen{position:absolute;left:17px;top:22px;width:381px;height:215px;
    background:linear-gradient(180deg,#000 0,#000 7%,#555 30%,#3a3a3a 80%,#000 91%)}
  .video-controls{position:absolute;left:17px;top:237px;width:381px;height:15px;background:#eee;border-top:3px solid #d22}
  .tile{position:absolute;width:279px;height:112px}
  .tile-photo{position:absolute;left:50px;top:3px;width:229px;height:100px;border-radius:50px;
    box-shadow:4px 4px 8px rgba(0,0,0,.18)}
  .tile-bubble{position:absolute;left:0;top:0;width:113px;height:113px;border-radius:50%;
    display:flex;align-items:center;justify-content:center;text-align:center;font-size:19px;line-height:24px;color:#1a1a1a}
  .tile-bubble::after{content:"";position:absolute;left:20px;bottom:-6px;border-top:14px solid var(--tail);border-right:16px solid transparent;transform:rotate(18deg)}
  .t-psychic{left:21px;top:745px}.t-therapist{left:312px;top:745px}.t-business{left:601px;top:745px}
  .t-career{left:21px;top:887px}.t-jobs{left:312px;top:887px}.t-product{left:601px;top:887px}
  .follow{position:absolute;left:0;top:1049px;width:897px;text-align:center;font-size:16px}
  .social{position:absolute;left:0;top:1080px;width:897px;display:flex;justify-content:center;gap:14px;font-size:14px;align-items:center}
  .social span{display:flex;align-items:center;gap:5px}
  .social b{width:12px;height:12px;background:var(--sea-mid);border-radius:2px}
  .footer-nav{position:absolute;left:0;top:1121px;width:897px;display:flex;justify-content:center;gap:14px;font-size:16px}
  .bottom-band{position:absolute;left:0;top:1151px;width:897px;height:49px;
    background:linear-gradient(180deg,var(--green-dark),var(--white) 35%,var(--green-light) 55%,var(--green-mid) 85%,var(--green-dark));
    text-align:center;font-size:16px;padding-top:10px}
</style>
</head>
<body>
<div class="site">
  <nav class="utility-nav"><span>contact us</span><span class="sep">|</span><span>sign in</span><span class="sep">|</span><span>register</span></nav>
  <div class="top-band"></div>
  <div class="logo-box"><span class="logo-dot"></span><span class="logo-name">kindred echo</span></div>

  <section class="hero">
    <div class="hero-photo" role="img" aria-label="Man dressed in white sitting cross-legged by the sea, pointing to the upper right"></div>
    <svg class="hero-panel" width="897" height="297" viewBox="0 0 897 297" aria-hidden="true">
      <defs>
        <linearGradient id="panelGreen" x1="0" y1="0" x2="1" y2="0">
          <stop offset="0" stop-color="#9ccb86"/><stop offset=".55" stop-color="#ffffff"/><stop offset="1" stop-color="#b7d9a3"/>
        </linearGradient>
      </defs>
      <path d="M0 0 H430 C380 8 350 40 340 110 L322 230 C312 275 290 297 250 297 H0 Z" fill="url(#panelGreen)"/>
      <path d="M430 0 C380 8 350 40 340 110 L322 230 C312 275 290 297 250 297" fill="none" stroke="#5f9a4a" stroke-width="5"/>
    </svg>
    <p class="hero-headline">How to gain<br>peace of mind<br>in daily life.</p>
  </section>

  <ul class="main-nav">
    <li>home</li><li>about us</li><li>latest news</li><li>community calendar</li><li>member search</li>
  </ul>
  <div class="join-btn">Join Now <i></i></div>

  <section class="intro">
    <h1>Welcome to our online community!</h1>
    <p>Welcome to Kindred Echo Community &amp; Chat Rooms. We hope you will explore the various features our websites has to offer. We created this online space for log on and create a dynamic member profile, collaborate on projects, share, your ideas and expertise - and most important, connect with your fellow members.</p>
    <p>Share, collaborate, exchange and grow - that's why we're here and we hope you are too. Engage and explore anytime, from anywhere there's a web connection.<br>Share. Learn. Grow.</p>
  </section>

  <div class="video-frame">
    <div class="video-screen" role="img" aria-label="Video still of a man sitting on the edge of a bed in a dim room"></div>
    <div class="video-controls"></div>
  </div>

  <a class="tile t-psychic"><div class="tile-photo" role="img" aria-label="Candle, tarot cards and old book" style="background:linear-gradient(90deg,#3a2410,#7a5a3a 40%,#2a0d1a)"></div><div class="tile-bubble" style="background:var(--pink);--tail:var(--pink)">find a<br>psychic</div></a>
  <a class="tile t-therapist"><div class="tile-photo" role="img" aria-label="Person receiving a relaxing head treatment" style="background:linear-gradient(90deg,#fbe7da,#f2c9b0 45%,#e8eef8)"></div><div class="tile-bubble" style="background:var(--orange);--tail:var(--orange)">find a<br>therapist</div></a>
  <a class="tile t-business"><div class="tile-photo" role="img" aria-label="Calm treatment room with golden curtains" style="background:linear-gradient(90deg,#b9a94a,#d8c86a 50%,#8c7d35)"></div><div class="tile-bubble" style="background:var(--lime);--tail:var(--lime)">find a<br>business/<br>school</div></a>
  <a class="tile t-career"><div class="tile-photo" role="img" aria-label="Hand writing with a pen on paperwork" style="background:linear-gradient(90deg,#f3ece6,#e9d2c3 50%,#f6f2ef)"></div><div class="tile-bubble" style="background:var(--apricot);--tail:var(--apricot)">hollistic<br>career<br>centre</div></a>
  <a class="tile t-jobs"><div class="tile-photo" role="img" aria-label="Jobs signpost against a blue sky" style="background:linear-gradient(90deg,#d9ecf7,#4a8ec6 50%,#2a6aa8)"></div><div class="tile-bubble" style="background:var(--cyan);--tail:var(--cyan)">hollistic<br>career<br>centre</div></a>
  <a class="tile t-product"><div class="tile-photo" role="img" aria-label="Glass oil bottles and a pink flower" style="background:linear-gradient(90deg,#d9a2d0,#f1d0ea 50%,#b44aa6)"></div><div class="tile-bubble" style="background:var(--plum);--tail:var(--plum)">find a<br>product</div></a>

  <p class="follow">follow us on:</p>
  <div class="social">
    <span><b></b>snapwell</span><span><b></b>chatterly</span><span><b></b>linkfolk</span><span><b></b>blurbo</span><span><b></b>feed</span>
  </div>
  <nav class="footer-nav">
    <span>home</span><span>|</span><span>contact us</span><span>|</span><span>archives</span><span>|</span><span>blogs</span><span>|</span><span>services</span><span>|</span><span>map to ur office</span>
  </nav>
  <footer class="bottom-band">@copyright 2011 www.calmgather.com all rights reserved</footer>
</div>
</body>
</html>
```